Animated GIF banner for mobile app

We need a GIF Banner designed that alternates between two different ads.

Details are;
Pixel Size (W X H) 300 X 250
Minimum DPI 72dpi
File Size 40kb
File Size (Rich Media) 150kb

Ad 1 Text:
Lost super? More than one super fund? Contact us

Ad 2 Text:
Time to review your home loan? Contact us

Target Market(s)

30-55 year olds

Industry/Entity Type

Financial Service

Font styles to use
Sans Serif

Colors
0555a3
3176b5
85abd2

```html
<!DOCTYPE html>
<html lang="en">
<head>
<meta charset="UTF-8">
<title>Harlow Reed Financial Solutions – Banner Set</title>
<link href="https://fonts.googleapis.com/css2?family=Arimo:wght@400;700&display=swap" rel="stylesheet">
<style>
  :root {
    --page-bg: #000000;
    --brand-blue: #0555a3;
    --brand-mid: #3176b5;
    --brand-light: #85abd2;
    --navy: #0b4a8f;
    --gold: #f7b52c;
    --gold-deep: #f0a81e;
    --ink: #0a0a0a;
    --white: #ffffff;
  }
  * { margin: 0; padding: 0; box-sizing: border-box; }
  html, body {
    width: 844px;
    height: 1200px;
    overflow: hidden;
    background: var(--page-bg);
    font-family: "Arimo", Arial, sans-serif;
  }
  .banner {
    position: absolute;
    left: 110px;
    width: 622px;
    height: 517px;
    overflow: hidden;
  }
  .banner--super { top: 59px; }
  .banner--loan { top: 599px; }

  .banner__photo {
    position: absolute;
    inset: 0;
  }
  .banner--super .banner__photo {
    background:
      radial-gradient(ellipse at 70% 30%, rgba(133,171,210,0.55), transparent 60%),
      linear-gradient(160deg, #6f8fcf 0%, var(--brand-mid) 45%, #2c4f9c 100%);
  }
  .banner--loan .banner__photo {
    background:
      radial-gradient(ellipse at 65% 30%, rgba(255,236,170,0.6), transparent 60%),
      linear-gradient(160deg, #f7cf6a 0%, #eebd45 50%, #d9a431 100%);
  }

  .brand-panel {
    position: absolute;
    left: 0;
    top: 0;
    width: 300px;
    height: 190px;
  }
  .brand-panel svg { position: absolute; inset: 0; }
  .brand-name {
    position: absolute;
    left: 18px;
    top: 40px;
    display: flex;
    align-items: center;
    gap: 12px;
    color: var(--brand-blue);
    font-weight: 400;
  }
  .brand-name__dot {
    width: 34px;
    height: 34px;
    border-radius: 50%;
    background: var(--brand-blue);
    flex: none;
  }
  .brand-name__text {
    font-size: 30px;
    line-height: 1.1;
    letter-spacing: -0.5px;
  }
  .brand-name__sub {
    display: block;
    font-size: 21px;
  }

  .banner__copy {
    position: absolute;
    left: 0;
    right: 0;
    text-align: center;
  }
  .headline {
    font-weight: 700;
    letter-spacing: -0.5px;
  }
  .banner--super .headline {
    color: var(--white);
    font-size: 76px;
    line-height: 1;
  }
  .banner--super .subline {
    color: var(--white);
    font-size: 30px;
    margin-top: 10px;
  }
  .banner--super .banner__copy { top: 240px; }

  .banner--loan .headline {
    color: var(--ink);
    font-size: 62px;
    line-height: 1.0;
  }
  .banner--loan .banner__copy { top: 250px; }

  .cta {
    position: absolute;
    left: 50%;
    transform: translateX(-50%);
    width: 245px;
    height: 56px;
    border-radius: 6px;
    display: flex;
    align-items: center;
    justify-content: center;
    font-size: 29px;
    font-weight: 700;
  }
  .banner--super .cta {
    top: 422px;
    background: var(--gold);
    color: var(--navy);
  }
  .banner--loan .cta {
    top: 420px;
    background: var(--navy);
    color: var(--white);
  }
</style>
</head>
<body>

<section class="banner banner--super">
  <div class="banner__photo" role="img" aria-label="Business people meeting in an office, with charts and a calculator on a desk, tinted blue"></div>
  <div class="brand-panel">
    <svg width="300" height="190" viewBox="0 0 300 190">
      <polygon points="0,0 300,0 236,190 0,190" fill="var(--gold-deep)"/>
      <polygon points="0,0 282,0 218,190 0,190" fill="var(--white)"/>
    </svg>
    <div class="brand-name">
      <span class="brand-name__dot"></span>
      <span class="brand-name__text">Harlow Reed<span class="brand-name__sub">Financial Solutions</span></span>
    </div>
  </div>
  <div class="banner__copy">
    <h1 class="headline">Lost super?</h1>
    <p class="subline">More than one super fund?</p>
  </div>
  <div class="cta">Contact Us</div>
</section>

<section class="banner banner--loan">
  <div class="banner__photo" role="img" aria-label="Business people meeting in an office, with charts and a calculator on a desk, tinted yellow"></div>
  <div class="brand-panel">
    <svg width="300" height="190" viewBox="0 0 300 190">
      <polygon points="0,0 300,0 236,190 0,190" fill="var(--brand-blue)"/>
      <polygon points="0,0 282,0 218,190 0,190" fill="var(--white)"/>
    </svg>
    <div class="brand-name">
      <span class="brand-name__dot"></span>
      <span class="brand-name__text">Harlow Reed<span class="brand-name__sub">Financial Solutions</span></span>
    </div>
  </div>
  <div class="banner__copy">
    <h1 class="headline">Time to review<br>your home loan?</h1>
  </div>
  <div class="cta">Contact Us</div>
</section>

</body>
</html>
```